Health Coach needs a Business Card Design

Need a really modern feminine business card design for a health and lifestyle coach. Needs to use geometric shapes, muted grey/blue/green pastels and black and white - see mood board attached and logo. The client likes black and white, modern, san serif with the use of lines and possibly a shadow leaf as in the mood board. Possibly put the tag line on the back or an icon of the logo. Logo is also attached. An icon of the logo would be great too.

Target Market(s)

Women (some men) aged 30 to 50.

Industry/Entity Type

Business

Contact Information for Business Card

Marla Teveny
e-mail: hello@marlatwell.example
website: marlatwell.example
Phone: +610497258316

The tag line is "Steady health for living"

Font styles to use
Sans Serif

Colors
ecf7fb
cfeae6
000000
ffffff
f5f5f5

Requirements
Must have
• Black and white, logo, tag line and details
Nice to have
• Would be nice to incorporate the shadow palm.fern leaves as in the mood board and or geometric lines/shapes - see mood board. Could be either standard rectangle or would be happy with square too.
Should not have
• Flowers or decorations

```html
<!DOCTYPE html>
<html lang="en">
<head>
<meta charset="utf-8">
<title>Marla T — Business Card</title>
<link rel="stylesheet" href="https://fonts.googleapis.com/css2?family=Josefin+Sans:wght@300;400&family=Cormorant+SC:wght@500&display=swap">
<style>
  :root {
    --stage: #e2e4e6;
    --card-white: #ffffff;
    --card-mist: #f5f5f5;
    --card-ice: #ecf7fb;
    --card-mint: #cfeae6;
    --ink: #000000;
    --ink-soft: #3a3a3a;
    --shade: rgba(0, 0, 0, 0.14);
  }
  * { box-sizing: border-box; margin: 0; padding: 0; }
  html, body {
    width: 1200px;
    height: 840px;
    overflow: hidden;
    background: var(--stage);
  }
  .canvas {
    position: relative;
    width: 1200px;
    height: 840px;
  }
  .card {
    position: absolute;
    background: linear-gradient(160deg, var(--card-white) 0%, var(--card-mist) 45%, var(--card-ice) 100%);
    box-shadow: 0 10px 28px var(--shade);
    overflow: hidden;
  }

  /* Front */
  .card--front {
    left: 130px;
    top: 150px;
    width: 330px;
    height: 540px;
  }
  .brand {
    position: absolute;
    top: 120px;
    left: 0;
    width: 100%;
    text-align: center;
  }
  .brand__name {
    font-family: "Josefin Sans", sans-serif;
    font-weight: 300;
    font-size: 34px;
    line-height: 40px;
    letter-spacing: 2px;
    color: var(--ink);
  }
  .brand__tagline {
    margin-top: 8px;
    font-family: "Josefin Sans", sans-serif;
    font-weight: 300;
    font-size: 9px;
    letter-spacing: 3px;
    color: var(--ink-soft);
    text-transform: uppercase;
  }
  .front-scene {
    position: absolute;
    top: 210px;
    left: 0;
    width: 100%;
    height: 140px;
    background: linear-gradient(90deg, #1c1c1c 0%, #9a9a9a 30%, #eeeeee 50%, #8f8f8f 70%, #1c1c1c 100%);
  }
  .contact {
    position: absolute;
    top: 385px;
    left: 0;
    width: 100%;
    text-align: center;
    font-family: "Cormorant SC", serif;
    font-weight: 500;
    color: var(--ink);
  }
  .contact__name {
    font-size: 15px;
    letter-spacing: 5px;
    text-transform: uppercase;
    margin-bottom: 8px;
  }
  .contact__rule {
    width: 250px;
    height: 1px;
    margin: 0 auto 20px;
    background: var(--ink);
  }
  .contact__line {
    font-size: 12px;
    letter-spacing: 2.5px;
    line-height: 17px;
  }

  /* Back */
  .card--back {
    left: 560px;
    top: 255px;
    width: 540px;
    height: 330px;
  }
  .back-scene {
    position: absolute;
    left: 110px;
    top: 30px;
    width: 270px;
    height: 230px;
    border-radius: 40% 50% 45% 55%;
    background: radial-gradient(ellipse at 45% 60%, #111111 0%, #2c2c2c 45%, rgba(60, 60, 60, 0.25) 75%, rgba(255, 255, 255, 0) 100%);
  }
  .back-tagline {
    position: absolute;
    right: 20px;
    top: 50%;
    writing-mode: vertical-rl;
    transform: translateY(-50%) rotate(180deg);
    white-space: nowrap;
    font-family: "Josefin Sans", sans-serif;
    font-weight: 300;
    font-size: 15px;
    letter-spacing: 3px;
    text-transform: uppercase;
    color: var(--ink);
  }
</style>
</head>
<body>
  <main class="canvas">
    <section class="card card--front">
      <div class="brand">
        <div class="brand__name">Marla T</div>
        <div class="brand__tagline">Steady health for living</div>
      </div>
      <div class="front-scene" role="img" aria-label="Black and white illustration of a woman with an umbrella in a rainy forest"></div>
      <div class="contact">
        <div class="contact__name">Marla Teveny</div>
        <div class="contact__rule"></div>
        <div class="contact__line">hello@marlatwell.example</div>
        <div class="contact__line">marlatwell.example</div>
        <div class="contact__line">+610497258316</div>
      </div>
    </section>

    <section class="card card--back">
      <div class="back-scene" role="img" aria-label="Black silhouette illustration of an open umbrella with a flock of birds rising from it"></div>
      <div class="back-tagline">Steady health for living</div>
    </section>
  </main>
</body>
</html>
```